Redesign B2B website

We are redesigning/ restructuring our current website. We provide company feedback surveys. We claim to be market leader in our country.
We like to be seen as a trustworthy, reliable and innovative partner to the top 1500 companies in the netherlands.
We want to be seen as a personal company.
Current website http://www.brivanto.nl does not meet our standards mentioned above.
Added Homepage layout. Please check
Target Market(s)
Large businesses, HR, decisiontakers
Industry/Entity Type
It Company
Requirements
Must have
- -The website is intended to be responsive. please take that into account. (propose plankor.es)
-The design should match our Style colors(will be provided)
- Wireframes are provided. Fonts used are Open Sans and Esteban,. Feel free to change things around.
Nice to have
- We like the design to be "flat", not much 3d effects, or icons.
Minimalist, Wordpress style or Metro style.

```html
<!DOCTYPE html>
<html lang="nl">
<head>
<meta charset="utf-8">
<title>Brivanto – Medewerkers- en klantenonderzoek</title>
<link href="https://fonts.googleapis.com/css2?family=Esteban&family=Open+Sans:wght@400;600;700&display=swap" rel="stylesheet">
<style>
:root{
  --navy:#0d2d4e;
  --navy-dark:#0a2440;
  --teal:#1b8a8c;
  --yellow:#f2c21a;
  --yellow-soft:#f3d98a;
  --text:#2a2a2a;
  --grey:#8d8d8d;
  --line:#1d3b5c;
  --white:#fff;
}
*{box-sizing:border-box;margin:0;padding:0}
html,body{width:945px;height:1200px;overflow:hidden;background:var(--white)}
body{position:relative;font-family:"Open Sans",Arial,sans-serif;color:var(--text)}
.abs{position:absolute}
.serif{font-family:"Esteban",Georgia,serif}

.brand-mark{left:96px;top:21px;width:171px;height:32px;border:1px solid var(--navy);display:flex;align-items:center;justify-content:center;gap:8px;font-weight:700;font-size:18px;letter-spacing:2px;color:var(--navy)}
.brand-mark .dot{width:14px;height:14px;border-radius:50%;background:var(--yellow)}
.call{font-weight:600;font-size:14px;color:var(--navy-dark)}
.social{display:flex;gap:9px}
.social span{width:16px;height:16px;border-radius:50%;background:var(--navy)}
.rule{left:0;width:945px;height:2px;background:var(--line)}

.nav{left:108px;top:88px;display:flex;gap:0;font-size:14.5px;color:var(--navy-dark)}
.nav a{padding:3px 12px 4px;text-decoration:none;color:inherit;margin-right:1px}
.nav a.active{background:var(--navy);color:var(--white);border-radius:2px}
.search{width:167px;height:23px;border:1px solid var(--teal);border-radius:2px;font-size:11.5px;color:#666;padding:3px 0 0 16px}
.search svg{position:absolute;right:6px;top:5px}

.contact-tab{left:904px;top:169px;width:44px;height:136px;background:var(--navy);border-radius:5px 0 0 5px;box-shadow:-1px 2px 3px rgba(0,0,0,.35)}
.contact-tab span{position:absolute;left:10px;top:98px;transform:rotate(-90deg);transform-origin:left top;color:var(--yellow);font-size:17px}

.hero-title{left:99px;top:153px;width:330px;font-size:19.5px;line-height:23px;color:var(--navy-dark)}
.hero-text{left:99px;width:330px;font-size:10.3px;line-height:18px}
.btn{left:267px;top:416px;width:141px;height:37px;background:var(--navy);color:var(--yellow);font-size:15px;display:flex;align-items:center;justify-content:center;border-radius:2px}

.video{left:450px;top:150px;width:398px;height:224px;border:2px solid #555;background:radial-gradient(ellipse at center,#fff 20%,#cfcfcf 100%)}
.video .title{position:absolute;left:72px;top:74px;width:250px;height:46px;border:3px solid var(--navy);display:flex;align-items:center;justify-content:center;gap:10px;font-weight:700;font-size:24px;letter-spacing:2px;color:var(--navy)}
.video .title .dot{width:18px;height:18px;border-radius:50%;background:var(--yellow)}
.video .sub{position:absolute;left:0;width:100%;top:126px;text-align:center;font-size:14px;color:#222}
.vbtn{position:absolute;right:6px;width:32px;height:25px;background:#3c3c3c;border-radius:3px;color:#fff;font-size:6px;font-weight:700;text-align:center;padding-top:15px}
.vbar{position:absolute;left:8px;right:8px;bottom:8px;height:28px;display:flex;gap:4px}
.vbar .play{width:48px;background:#2e2e2e;border-radius:3px}
.vbar .track{flex:1;background:#2e2e2e;border-radius:3px;position:relative}
.vbar .track i{position:absolute;left:6px;right:140px;top:11px;height:7px;border:1px solid #999}
.thumbs{left:450px;top:377px;width:398px;height:71px}
.arrow-btn{width:32px;height:71px;background:#9b9b9b;color:#fff;font-size:24px;display:flex;align-items:center;justify-content:center}
.thumb{top:0;width:102px;height:71px}

.feature-icon{left:98px;width:77px;height:77px;border:1px solid var(--yellow);border-radius:2px;display:flex;align-items:center;justify-content:center;font-size:13px;font-weight:700}
.feature-title{left:190px;font-size:18.5px;color:var(--teal)}
.feature-text{left:192px;width:360px;font-size:9.6px;line-height:18px}

.quote{left:583px;top:512px;width:275px;font-size:17px;line-height:27px;font-style:italic;color:#222}
.quote-by{left:742px;top:655px;display:flex;align-items:center;gap:8px;font-style:italic;font-size:12px;color:var(--teal)}
.quote-by span.sq{width:22px;height:22px;background:var(--navy)}

.clients{left:581px;top:699px;width:267px;height:133px;border:1px solid var(--yellow);border-radius:2px}
.clients h3{position:absolute;left:13px;top:9px;font-size:16.5px;font-style:italic;font-weight:400;color:var(--navy-dark)}
.client-grid{position:absolute;left:10px;top:45px;width:250px;display:grid;grid-template-columns:repeat(3,1fr);row-gap:22px;font-size:13px;font-weight:600;color:var(--navy);text-align:center}

.footer-call{font-weight:600;font-size:14px;color:var(--navy-dark)}
.col{top:938px;font-size:9.5px;line-height:18px;color:#333}
.col h4{font-family:"Esteban",Georgia,serif;font-weight:400;font-size:16.5px;color:var(--navy-dark);margin-bottom:14px}
.legal{top:1161px;left:0;width:945px;text-align:center;font-size:9.5px;color:#333}
.legal a{color:var(--teal);text-decoration:none}
</style>
</head>
<body>

<header>
  <div class="abs brand-mark"><span>BRIVANTO</span><span class="dot"></span></div>
  <div class="abs call" style="left:550px;top:25px">CALL US ON - 020 4180733</div>
  <div class="abs social" style="left:736px;top:26px" aria-label="Sociale media"><span></span><span></span><span></span><span></span><span></span></div>
  <div class="abs rule" style="top:74px"></div>
  <nav class="abs nav">
    <a class="active">Producten</a><a>Opllosingen</a><a>Branches</a><a>Kennis</a><a>Klanten</a><a>Over Brivanto</a>
  </nav>
  <div class="abs search" style="left:681px;top:93px">Zoeken
    <svg width="10" height="10" viewBox="0 0 10 10"><circle cx="4" cy="4" r="3" fill="none" stroke="#555" stroke-width="1.4"/><line x1="6.3" y1="6.3" x2="9.3" y2="9.3" stroke="#555" stroke-width="1.5"/></svg>
  </div>
  <div class="abs rule" style="top:128px"></div>
</header>

<div class="abs contact-tab"><span>Contact</span></div>

<section>
  <h1 class="abs hero-title serif" style="font-weight:400">Bevlogenheild en betrokkenheid stimuleren binnen uw organisatie?</h1>
  <p class="abs hero-text" style="top:217px">Lorem Ipsum is simply dummy text of the printing and typesetting industry. Lorem Ipsum has been the industry's standard dummy text ever since the 1500s, when an unknown printer took a galley of type and scrambled it to make a type specimen book.</p>
  <p class="abs hero-text" style="top:307px">Lorem Ipsum is simply dummy text of the printing and typesetting industry. Lorem Ipsum has been the industry's standard dummy text ever since the 1500s, when an unknown printer took a galley of type and scrambled it to make a type specimen book.</p>
  <div class="abs btn">Gratis eBook</div>

  <div class="abs video">
    <div class="vbtn" style="top:7px">LIKE</div>
    <div class="vbtn" style="top:36px">LATER</div>
    <div class="vbtn" style="top:65px">SHARE</div>
    <div class="vbtn" style="top:94px">EMBED</div>
    <div class="title"><span>BRIVANTO</span><span class="dot"></span></div>
    <div class="sub">Medewerkers- en klantenonderzoek</div>
    <div class="vbar">
      <div class="play"><svg width="48" height="28"><rect x="18" y="8" width="4" height="12" fill="#fff"/><rect x="26" y="8" width="4" height="12" fill="#fff"/></svg></div>
      <div class="track"><i></i></div>
    </div>
  </div>
  <div class="abs thumbs">
    <div class="abs arrow-btn" style="left:0;top:0">«</div>
    <div class="abs thumb" role="img" aria-label="Videostill: man in pak aan het woord" style="left:36px;background:linear-gradient(135deg,#2a3b55,#8a8f99)"></div>
    <div class="abs thumb" role="img" aria-label="Videostill: titelkaart over de visie" style="left:149px;background:linear-gradient(180deg,#f4f0d0,#d9d9d9 80%,#0d2d4e 80%)"></div>
    <div class="abs thumb" role="img" aria-label="Videostill: vrouw aan het werk" style="left:263px;background:linear-gradient(135deg,#3a2c22,#b69a7e)"></div>
    <div class="abs arrow-btn" style="left:366px;top:0">»</div>
  </div>
</section>

<section>
  <div class="abs feature-icon" style="top:506px;color:#c98a12">Marwelde</div>
  <h2 class="abs feature-title serif" style="top:503px;font-weight:400">Een onderzoek dat bij past</h2>
  <p class="abs feature-text" style="top:528px">Lorem Ipsum is simply dummy text of the printing and typesetting industry. Lorem Ipsum has been the industry's standard dummy text ever since the 1500s when an unknown printer took a galley of type and scrambled it to make a type</p>

  <div class="abs feature-icon" role="img" aria-label="Illustratie: blauwe golf" style="top:612px;background:linear-gradient(#fff,#fff) padding-box"><svg width="50" height="40"><ellipse cx="25" cy="20" rx="22" ry="14" fill="#2aa6d8"/></svg></div>
  <h2 class="abs feature-title serif" style="top:609px;font-weight:400">Uw scores in prespectief met uw branche</h2>
  <p class="abs feature-text" style="top:634px">There are many variations of passages of Lorem Ipsum available, but the majority have suffered alteration in some form, by injected humour, or randomised words which don't look even slightly believable. If you are going to use a passage of Lorem Ipsum, you need to be sure there isn't anything.</p>

  <div class="abs feature-icon" style="top:733px;color:#e0611c">Tevanto</div>
  <h2 class="abs feature-title serif" style="top:729px;font-weight:400">Aan de slag met de resultaten</h2>
  <p class="abs feature-text" style="top:755px">It was popularised in the 1960s with the release of Letraset sheets containing Lorem Ipsum passages, and more recently with desktop publishing software like Aldus PageMaker including versions of Lorem Ipsum.</p>

  <blockquote class="abs quote serif">"Het beeld dat de medewerkers hebben met betrekking tot klantgerichtheid wordt in hoge mate bevestigd door de cliënten en ouders/verwanten. Daar zijn we erg blij mee!"</blockquote>
  <div class="abs quote-by serif"><span class="sq"></span>- VLIET, ORVANE</div>

  <div class="abs clients">
    <h3 class="serif">Onze klanten</h3>
    <div class="client-grid">
      <span>Ravento</span><span>Bloemveld</span><span>Nodara</span>
      <span>Kelmbank</span><span>Trevalo</span><span>Velta</span>
    </div>
  </div>
</section>

<footer>
  <div class="abs rule" style="top:859px"></div>
  <div class="abs footer-call" style="left:101px;top:877px">CALL US ON - 020 4180733</div>
  <div class="abs social" style="left:287px;top:879px" aria-label="Sociale media"><span></span><span></span><span></span><span></span><span></span></div>
  <div class="abs search" style="left:681px;top:875px;padding-left:8px">Nieuwsbrief
    <svg width="10" height="10" viewBox="0 0 10 10"><circle cx="4" cy="4" r="3" fill="none" stroke="#555" stroke-width="1.4"/><line x1="6.3" y1="6.3" x2="9.3" y2="9.3" stroke="#555" stroke-width="1.5"/></svg>
  </div>
  <div class="abs rule" style="top:912px"></div>

  <div class="abs col" style="left:101px"><h4>Wat doen wij</h4>Werken bij Brivanto<br>Open sollicitaties<br>Starters en professionals<br>Bijbanen en stages voor</div>
  <div class="abs col" style="left:266px"><h4>Intern klantenonderzoek</h4>Waarom intern klanteno<br>Werkwijze<br>Intern klanttevredenheid<br>Kwaliteit van stafafdelingen<br>Intern samenwerking<br>Projectevaluatie<br>Praktijkvoorbeelden<br>Prijsinformatie</div>
  <div class="abs col" style="left:496px"><h4>Informatie aanvragen</h4>Prijsinformatie aanvragen<br>Workshop medewerkers<br>Gratis boek 'Winnen met<br>Gratis boek '12 Gouden<br>Aanmelden Beste Werkgeve<br>Direct een afspraak maken<br>Gratis stappenplan: Werk aa</div>
  <div class="abs col" style="left:727px"><h4>Nieuws</h4>Nieuwsarchief<br>Inschrijven voor de<br>Inschrijven voor de<br>Uitschrijven voor de<br>Brivanto op Kringnet</div>

  <div class="abs rule" style="top:1146px"></div>
  <div class="abs legal">© 2012 Brivanto. Medewerkers- en klantenonderzoek &nbsp;&nbsp;&nbsp;&nbsp; <a>Disclaimer</a> &nbsp;&nbsp; | &nbsp;&nbsp; <a>Algemene Voorwaarden</a></div>
</footer>

</body>
</html>
```